Pest Control Flyer

I need a non tri fold flyer that will be placed door to door about 9 in long and 4 in wide. My company name is Copper Ridge Pest and Termite.
phone number is 555-214-3960. Company theme is RED WHITE & BLUE
we do guarantee our services, (dont say anything about money back guarantee ) Leave area rep / rout manager blank so we can write in it. Please add our number.
local family owned company
Services pest control, rodent control, termite treatments, mosquito services , German Roach clean outs and many more!
Discounted pricing for new customers and referrals get up to $100.00 off your initial pest control service

```html
<!DOCTYPE html>
<html lang="en">
<head>
<meta charset="utf-8">
<title>Copper Ridge Pest and Termite – Door Flyer</title>
<link href="https://fonts.googleapis.com/css2?family=Montserrat:ital,wght@0,500;0,600;0,700;0,800;1,800&display=swap" rel="stylesheet">
<style>
  :root{
    --blue:#17498a;
    --red:#d42229;
    --white:#ffffff;
    --ring:#9db3d4;
    --ink:#0d0d0d;
  }
  *{margin:0;padding:0;box-sizing:border-box}
  html,body{width:1200px;height:2492px;overflow:hidden;background:var(--white)}
  .flyer{position:relative;width:1200px;height:2492px;background:var(--blue);
    font-family:"Montserrat",sans-serif;color:var(--white);overflow:hidden}
  .flyer__chevron{position:absolute;left:0;top:0}
  .brand-mark{position:absolute;left:0;width:1200px;top:170px;text-align:center}
  .brand-mark__dot{width:120px;height:120px;border-radius:50%;background:var(--blue);margin:0 auto 28px}
  .brand-mark__name{font-weight:800;font-size:56px;line-height:1.1;color:var(--blue);letter-spacing:2px}
  .title{position:absolute;left:0;width:1200px;text-align:center}
  .title__name{top:820px;font-weight:700;font-size:112px;letter-spacing:1px;line-height:1}
  .title__trade{top:950px;font-weight:500;font-size:96px;letter-spacing:2px;line-height:1}
  .write-in{position:absolute;left:77px;top:1133px;width:1025px;height:384px;
    background:var(--white);border-radius:90px}
  .tagline{position:absolute;left:170px;top:1088px;width:860px;height:62px;background:var(--blue);
    border-radius:0 0 40px 40px;text-align:center;font-weight:600;font-size:43px;line-height:62px;letter-spacing:1px}
  .contact{position:absolute;left:250px;top:1490px;width:700px;height:110px;background:var(--blue);
    border-radius:40px 40px 0 0;text-align:center}
  .contact__phone{font-weight:600;font-size:86px;line-height:1;padding-top:18px}
  .contact__note{position:absolute;left:0;width:1200px;top:1596px;text-align:center;font-weight:500;font-size:42px}
  .service{position:absolute;width:440px;text-align:center;transform:translateX(-50%)}
  .service__icon{display:block;margin:0 auto}
  .service__label{font-weight:600;font-size:30px;line-height:1.05;margin-top:4px;white-space:nowrap}
  .offer{position:absolute;left:0;top:2292px;width:1200px;height:200px;background:var(--white);text-align:center}
  .offer__lead{font-weight:700;font-size:27px;line-height:1.2;color:var(--blue);padding-top:18px}
  .offer__deal{font-weight:800;font-size:80px;color:var(--ink);line-height:1;margin-top:8px}
  .offer__deal em{color:var(--red);font-style:italic}
  .offer__tail{font-weight:700;font-size:33px;line-height:1.2;color:var(--blue);margin-top:8px}
</style>
</head>
<body>
<main class="flyer">
  <svg class="flyer__chevron" width="1200" height="770" viewBox="0 0 1200 770" aria-hidden="true">
    <polygon points="0,0 1200,0 1200,137 600,765 0,137" fill="#ffffff"/>
  </svg>

  <div class="brand-mark">
    <div class="brand-mark__dot"></div>
    <div class="brand-mark__name">COPPER RIDGE</div>
  </div>

  <h1 class="title title__name">COPPER RIDGE</h1>
  <p class="title title__trade">PEST AND TERMITE</p>

  <div class="write-in" aria-label="Area rep / route manager write-in space"></div>
  <p class="tagline">WE DO GUARANTEE OUR SERVICES</p>
  <div class="contact"><p class="contact__phone">555-214-3960</p></div>
  <p class="contact__note">LOCAL FAMILY OWNED COMPANY</p>

  <div class="service" style="left:216px;top:1700px">
    <svg class="service__icon" width="200" height="200" viewBox="0 0 224 224" aria-hidden="true">
      <circle cx="112" cy="112" r="106" fill="var(--red)" stroke="var(--ring)" stroke-width="8"/>
      <circle cx="112" cy="112" r="58" fill="none" stroke="#fff" stroke-width="7"/>
      <path d="M112 40v30M112 154v30M40 112h30M154 112h30" stroke="#fff" stroke-width="7"/>
      <ellipse cx="112" cy="116" rx="18" ry="26" fill="#fff"/>
      <circle cx="112" cy="86" r="10" fill="#fff"/>
    </svg>
    <p class="service__label">Services pest<br>control</p>
  </div>

  <div class="service" style="left:600px;top:1700px">
    <svg class="service__icon" width="200" height="200" viewBox="0 0 224 224" aria-hidden="true">
      <circle cx="112" cy="112" r="106" fill="var(--red)" stroke="var(--ring)" stroke-width="8"/>
      <ellipse cx="108" cy="132" rx="42" ry="24" fill="#fff"/>
      <circle cx="70" cy="124" r="18" fill="#fff"/>
      <path d="M148 138c20 0 22-30 14-50" stroke="#fff" stroke-width="5" fill="none"/>
    </svg>
    <p class="service__label">Rodent Control</p>
  </div>

  <div class="service" style="left:980px;top:1700px">
    <svg class="service__icon" width="200" height="200" viewBox="0 0 224 224" aria-hidden="true">
      <circle cx="112" cy="112" r="106" fill="var(--red)" stroke="var(--ring)" stroke-width="8"/>
      <circle cx="112" cy="70" r="14" fill="#fff"/>
      <ellipse cx="112" cy="100" rx="16" ry="14" fill="#fff"/>
      <ellipse cx="112" cy="142" rx="24" ry="32" fill="#fff"/>
      <path d="M96 100l-30-12M128 100l30-12M92 130l-32 4M132 130l32 4M96 160l-24 20M128 160l24 20" stroke="#fff" stroke-width="5"/>
    </svg>
    <p class="service__label">Termite<br>Treatments</p>
  </div>

  <div class="service" style="left:404px;top:1985px">
    <svg class="service__icon" width="200" height="200" viewBox="0 0 224 224" aria-hidden="true">
      <circle cx="112" cy="112" r="106" fill="var(--red)" stroke="var(--ring)" stroke-width="8"/>
      <ellipse cx="122" cy="126" rx="16" ry="40" fill="#fff" transform="rotate(-35 122 126)"/>
      <ellipse cx="84" cy="86" rx="12" ry="28" fill="#fff" transform="rotate(-50 84 86)"/>
      <path d="M100 130l-40 40M112 140l-10 50M130 140l40 40M70 90l-30-30" stroke="#fff" stroke-width="5"/>
    </svg>
    <p class="service__label">Mosquito<br>Services</p>
  </div>

  <div class="service" style="left:788px;top:1985px">
    <svg class="service__icon" width="200" height="200" viewBox="0 0 224 224" aria-hidden="true">
      <circle cx="112" cy="112" r="106" fill="var(--red)" stroke="var(--ring)" stroke-width="8"/>
      <ellipse cx="112" cy="122" rx="30" ry="44" fill="#fff"/>
      <circle cx="112" cy="72" r="13" fill="#fff"/>
      <path d="M104 62l-20-24M120 62l20-24M82 104l-26-10M142 104l26-10M82 128l-30 4M142 128l30 4M86 150l-22 22M138 150l22 22" stroke="#fff" stroke-width="5"/>
      <path d="M112 84v80" stroke="var(--red)" stroke-width="3"/>
    </svg>
    <p class="service__label">German Roach clean<br>outs and many more!</p>
  </div>

  <section class="offer">
    <p class="offer__lead">DISCOUNTED PRICING FOR NEW CUSTOMERS AND REFERRALS GET</p>
    <p class="offer__deal">Up to <em>$100.00 OFF</em></p>
    <p class="offer__tail">YOUR INITIAL PEST CONTROL SERVICE</p>
  </section>
</main>
</body>
</html>
```